依頼詳細
ダウンロードデータ内にサイトマップとデザイン制作要望を準備しています。
現行サイトURLはデータ内でご確認ください。

◆サイトマップ
1.TOP
└2.当サロンについて
└3.初めての方へ
└4.頭皮・髪質改善へのこだわり
└5.髪質のお悩み
└6.カラーダメージのお悩み
└7.頭皮のお悩み
└8.お悩みビフォー・アフター
└9.VORA公式アプリ
└10.Q&A
└11.MENU・COUPON
└12.PRODUCT
└13.STAFF(一覧)
└14.VOICE(一覧)
└15.NEWS・BLOG(一覧)
└16.RECRUIT
└17.CONTACT

◆希望デザインカラー
希望テイストに合わせて色を使用いただきたいですが、すべて茶系・モノクロなど暗いイメージにならないようにゴールドや明るい色をポイントで使用いただきたいです。

◆デザインのテイスト・イメージ
・高級感(上品な高級感)
・清潔
・見やすさのユーザビリティとお洒落さを取り入れたデザイン

◆参考イメージ
https://beautyroom-marnel-example.com/
①ターゲット層に好まれるデザインだと感じました。
(色の配色、キラキラした背景やグラデーションのバランス)
②コンテンツ毎にデザインが異なり、目に止まりやすいと感じました。
③文章量がちょうど良く、直感的に内容を把握できる
(同じくらいの文章量・余白を希望します)
明るくデザインに映える色をポイントで使用
• イラストレーター形式 (.ai)
• フォトショップ形式 (.psd)
【素材・データ】
①制作要望・素材写真
制作要望・素材写真について、下記よりダウンロードしてご使用ください。
https://filedepot-sample.jp/download/9a1c7e5b20d84f36a0be7c1d92f4e6a8b3c5d7f1
ダウンロードパスワード q8wm2tv6
また、現行サイトの素材や内容を使用頂いても問題ありません。
ロゴは現行サイトから使用下さい。

②写真(その他)
Pictora Bank[ https://images.pictorabank-sample.com/jp/]で定期契約をしています。
また定期契約のものは弊社の負担となり、ランサー様に負担はありません。
カンプ画像を入れてください。
その際、通常アセットで購入できる画像でお願いいたします。

③その他
・業務への支障がでる可能性がございますので、店舗へ直接の連絡はお控え下さい。
・申し訳ございませんがXD形式の納品はお受けできかねます。
・デザインの横幅は1300pxで作成お願いいたします。
どうぞ自由な発想でご提案ください。

```html
<!DOCTYPE html>
<html lang="ja">
<head>
<meta charset="UTF-8">
<title>緑ヶ丘市の美容室 ヴォーラ</title>
<link href="https://fonts.googleapis.com/css2?family=Shippori+Mincho:wght@400;600&family=Noto+Sans+JP:wght@400;500&display=swap" rel="stylesheet">
<style>
:root{
  --orange:#f08a3c;
  --orange-light:#f7a760;
  --gold:#e8b95a;
  --cream:#f8ecd8;
  --beige:#f1e2d3;
  --ink:#3d3330;
  --muted:#7a6d66;
  --white:#ffffff;
  --line:#e9c98f;
}
*{margin:0;padding:0;box-sizing:border-box}
html,body{width:1200px;height:5028px;overflow:hidden}
body{position:relative;background:var(--white);color:var(--ink);font-family:"Noto Sans JP",sans-serif;font-size:15px;line-height:1.8}
.abs{position:absolute}
.btn{position:absolute;display:flex;align-items:center;justify-content:center;border-radius:40px;background:linear-gradient(90deg,var(--orange-light),var(--orange));color:var(--white);font-size:14px;letter-spacing:.08em;box-shadow:0 4px 10px rgba(240,138,60,.25);white-space:nowrap}
.btn::after{content:"›";margin-left:10px}
.section-title{position:absolute;left:0;width:1200px;text-align:center;font-family:"Shippori Mincho",serif;font-size:30px;letter-spacing:.06em}
.photo{position:absolute}

/* header + hero */
.site-tagline{left:40px;top:24px;font-size:15px;color:var(--muted);font-family:"Shippori Mincho",serif}
.menu-toggle{right:140px;top:18px;width:56px}
.menu-toggle span{display:block;height:3px;background:var(--orange);margin:8px 0;border-radius:2px}
.menu-toggle small{position:absolute;top:-10px;left:12px;font-size:10px;color:var(--orange)}
.hero-photo{left:480px;top:0;width:720px;height:820px;background:radial-gradient(ellipse at 55% 35%,#f4ddc8 0%,#ece4dc 45%,#f7f4f1 80%)}
.brand{left:160px;top:212px;display:flex;align-items:center;gap:14px;font-family:"Shippori Mincho",serif;font-size:46px;letter-spacing:.3em;color:var(--ink)}
.brand i{width:12px;height:12px;border-radius:50%;background:var(--gold);display:block}
.hero-lead{left:160px;top:388px;font-family:"Shippori Mincho",serif;font-size:30px;letter-spacing:.08em}
.hero-catch{left:160px;top:440px;font-family:"Shippori Mincho",serif;font-size:52px;color:var(--orange);letter-spacing:.06em;white-space:nowrap}
.hero-catch small{font-size:34px;color:var(--ink)}
.hero-wave{left:0;top:770px}

/* news */
.news-box{left:260px;top:1000px;width:680px;height:48px;border:3px solid var(--gold);background:#fffbe9;display:flex;align-items:center;gap:28px;padding:0 20px;font-size:13px}
.news-box time{color:var(--muted)}
.more-link{position:absolute;display:flex;align-items:center;gap:10px;font-size:13px}
.more-link::before{content:"";width:60px;height:1px;background:var(--ink)}
.more-link i{width:36px;height:36px;border-radius:50%;background:var(--orange);color:var(--white);font-style:normal;display:flex;align-items:center;justify-content:center}

/* concept */
.concept-photo{left:180px;top:1172px;width:380px;height:468px;border-radius:40px 0 90px 0;background:linear-gradient(160deg,#d8b89a,#a8775a 60%,#6e4c3a)}
.concept-title{left:600px;top:1168px;font-family:"Shippori Mincho",serif;font-size:32px}
.concept-catch{left:600px;top:1232px;width:460px;color:var(--orange);font-family:"Shippori Mincho",serif;font-size:15px;line-height:1.9}
.concept-text{left:600px;top:1380px;width:460px;font-size:13px;color:var(--ink);line-height:2}
.concept-text p{margin-bottom:14px}

/* worries */
.worries{left:160px;top:1780px;width:888px;height:508px;background:var(--cream)}
.worries-title{position:absolute;top:36px;width:100%;text-align:center;font-family:"Shippori Mincho",serif;font-size:20px}
.worry{position:absolute;top:100px;width:220px;text-align:center;font-size:13px}
.worry .circle{width:170px;height:170px;border-radius:50%;margin:18px auto 28px;border:6px solid var(--white)}
.worry .btn{position:static;width:150px;height:36px;margin:0 auto;font-size:12px}
.worries .all-btn{left:274px;top:428px;width:340px;height:40px;font-size:13px}

/* menu */
.menu-sub{left:0;top:2452px;width:1200px;text-align:center;color:var(--orange);font-family:"Shippori Mincho",serif;font-size:17px}
.menu-band{left:0;top:2520px;width:1200px;height:600px;background:linear-gradient(90deg,#fff6d8 0%,#fde6a8 45%,#fbd98f 70%,#fff1d0 100%)}
.menu-text{left:260px;top:2620px;width:360px;font-size:14px;line-height:2.1;font-family:"Shippori Mincho",serif}
.menu-text em{font-style:normal;color:var(--orange)}

/* voice/product */
.banner{position:absolute;top:3260px;width:320px;height:140px;background:linear-gradient(120deg,#5b4637,#8a6b55);display:flex;flex-direction:column;align-items:center;justify-content:center;color:var(--white);font-family:"Shippori Mincho",serif;font-size:30px;letter-spacing:.1em;line-height:1.3}
.banner small{font-size:12px;letter-spacing:.05em}

/* staff */
.staff{position:absolute;top:3600px;width:120px;text-align:center;font-size:11px}
.staff .pic{height:140px;margin-bottom:10px}

/* footer */
.footer{left:0;top:4160px;width:1200px;height:868px;background:var(--beige)}
.footer .brand{top:200px;left:160px;font-size:40px}
.footer-name{left:160px;top:270px;font-family:"Shippori Mincho",serif;font-size:26px}
.footer-info{left:160px;top:326px;font-size:14px;line-height:1.9}
.footer-info .tel{font-size:20px;color:var(--ink)}
.app-btn{left:700px;top:250px;width:280px;height:56px;border:2px solid var(--white);background:var(--orange-light);color:var(--white);display:flex;align-items:center;justify-content:center;font-size:15px}
.sns{top:334px;width:30px;height:30px;border-radius:6px;background:var(--orange)}
.sitemap-label{left:160px;top:514px;font-size:12px;color:var(--muted)}
.sitemap{top:548px;list-style:none;font-size:13px;line-height:2}
.sitemap li::before{content:"> ";color:var(--orange)}
.copyright{left:0;top:830px;width:1200px;text-align:center;font-size:11px;color:var(--muted)}
</style>
</head>
<body>

<header>
  <p class="abs site-tagline">緑ヶ丘市の美容室　ヴォーラ</p>
  <div class="abs menu-toggle" aria-label="メニュー"><small>MENU</small><span></span><span></span><span></span></div>
</header>

<section class="hero">
  <div class="photo hero-photo" role="img" aria-label="明るい室内で微笑む大人の女性のポートレート写真"></div>
  <div class="abs brand"><i></i>VORA</div>
  <p class="abs hero-lead">髪や頭皮の悩みを抱える</p>
  <p class="abs hero-catch">オトナ女性<small>のための美容院</small></p>
  <a class="btn" style="left:200px;top:660px;width:340px;height:76px;font-size:20px">WEB予約はこちら</a>
  <svg class="abs hero-wave" width="1200" height="100" viewBox="0 0 1200 100">
    <path d="M0 40 C300 110 700 110 1200 0 L1200 100 L0 100Z" fill="#fff"/>
    <path d="M0 40 C300 110 700 110 1200 0" stroke="#f7a760" stroke-width="6" fill="none"/>
    <path d="M0 56 C320 120 760 100 1200 20" stroke="#fbd98f" stroke-width="3" fill="none"/>
  </svg>
</section>

<section class="news">
  <h2 class="section-title" style="top:936px;text-align:left;left:260px;width:auto">News &amp; Blog</h2>
  <div class="abs news-box"><time>2020.05.20</time><span>ホームページをリニューアルいたしました。</span></div>
  <a class="more-link" style="left:820px;top:1062px">一覧<i>›</i></a>
</section>

<section class="concept">
  <div class="photo concept-photo" role="img" aria-label="店内の壁に飾られたドライフラワーの写真"></div>
  <h2 class="abs concept-title">Concept</h2>
  <p class="abs concept-catch">「髪が細い・広がる」<br>「髪の傷み・頭皮・白髪が気になる」<br>などのお悩みを抱えるオトナ女性のための美容院</p>
  <div class="abs concept-text">
    <p>30代を中心に年齢を重ねるごとに増えていく、髪や頭皮の悩みに寄り添いながら、一人ひとりに合った提案をしています。</p>
    <p>お客様のお悩みやご希望を丁寧にお伺いし、それぞれに合わせた施術を心がけております。</p>
    <p>スタッフ一同、心よりご来店をお待ちしております。</p>
  </div>
  <a class="btn" style="left:880px;top:1556px;width:180px;height:34px;font-size:12px">当サロンについて</a>
  <a class="btn" style="left:880px;top:1614px;width:180px;height:34px;font-size:12px">初めての方へ</a>
</section>

<section class="abs worries">
  <h2 class="worries-title">— VORAが得意とするお悩み —</h2>
  <div class="worry" style="left:60px">髪質のお悩み<div class="circle" role="img" aria-label="髪の広がりに悩む女性の写真" style="background:linear-gradient(160deg,#e9ded6,#6b5448)"></div><a class="btn">詳しく見る</a></div>
  <div class="worry" style="left:334px">カラーダメージのお悩み<div class="circle" role="img" aria-label="傷んだ毛先のアップ写真" style="background:linear-gradient(160deg,#d8b89a,#8a5f45)"></div><a class="btn">詳しく見る</a></div>
  <div class="worry" style="left:608px">頭皮のお悩み<div class="circle" role="img" aria-label="頭皮をケアする手元の写真" style="background:linear-gradient(160deg,#c9a58c,#6e4c3a)"></div><a class="btn">詳しく見る</a></div>
  <a class="btn all-btn">頭皮・髪質改善へのこだわり</a>
</section>

<section class="menu">
  <h2 class="section-title" style="top:2396px">Menu</h2>
  <p class="abs menu-sub">ツヤメイクカラーやオゾンパーマが人気！</p>
  <div class="abs menu-band"></div>
  <div class="abs menu-text">
    <p>お客様のお悩みを解決するために<br>様々なメニュー、システムをご用意しております。</p><br>
    <p>カラーをすればするほど<br>髪が艶やかになる<em>ツヤメイクカラー</em>、<br>パーマをかければかけるほど<br>髪がしなやかに扱いやすくなる<em>オゾンパーマ</em>は<br>VORA独自の技術であり、特におすすめです。</p>
  </div>
  <a class="btn" style="left:380px;top:2990px;width:180px;height:38px;font-size:12px">メニュー詳細</a>
  <div class="photo" role="img" aria-label="ショートボブのスタイル写真" style="left:620px;top:2532px;width:200px;height:200px;background:linear-gradient(160deg,#cbb8a8,#6a4a38)"></div>
  <div class="photo" role="img" aria-label="ボブスタイルの後ろ姿の写真" style="left:840px;top:2740px;width:200px;height:200px;background:linear-gradient(160deg,#d6c4b2,#5e4131)"></div>
  <div class="photo" role="img" aria-label="カラー後のショートヘアの写真" style="left:620px;top:2940px;width:200px;height:180px;background:linear-gradient(160deg,#c4a890,#7b5238)"></div>
</section>

<section class="links">
  <a class="banner" style="left:220px" role="img" aria-label="お客様の声のバナー写真">VOICE<small>～お客様の声～</small></a>
  <a class="banner" style="left:660px" role="img" aria-label="取扱商品のバナー写真">PRODUCT<small>～取扱商品のご案内～</small></a>
</section>

<section class="staff-list">
  <h2 class="section-title" style="top:3496px;text-align:left;left:272px;width:auto">Staff</h2>
  <div class="staff" style="left:272px"><div class="pic" role="img" aria-label="男性スタイリストの写真" style="background:linear-gradient(160deg,#c8ae96,#4e3a2e)"></div>代表　山野</div>
  <div class="staff" style="left:448px"><div class="pic" role="img" aria-label="男性スタイリストの写真" style="background:linear-gradient(160deg,#d2baa4,#5a4032)"></div>店長　柏木</div>
  <div class="staff" style="left:624px"><div class="pic" role="img" aria-label="女性スタイリストの写真" style="background:linear-gradient(160deg,#d9c3ae,#6b4733)"></div>村瀬　千夏</div>
  <div class="staff" style="left:800px"><div class="pic" role="img" aria-label="女性スタイリストの写真" style="background:linear-gradient(160deg,#e0cbb8,#7b5843)"></div>浜口　結衣</div>
  <a class="more-link" style="left:900px;top:3790px">一覧<i>›</i></a>
</section>

<a class="btn" style="left:420px;top:3972px;width:360px;height:80px;font-size:20px">WEB予約はこちら</a>

<footer class="abs footer">
  <svg class="abs" style="left:0;top:-40px" width="1200" height="80" viewBox="0 0 1200 80">
    <path d="M0 40 C400 0 800 80 1200 30 L1200 80 L0 80Z" fill="#f1e2d3"/>
    <path d="M0 40 C400 0 800 80 1200 30" stroke="#f7a760" stroke-width="4" fill="none"/>
  </svg>
  <div class="abs brand"><i></i>VORA</div>
  <p class="abs footer-name">緑ヶ丘市の美容室ヴォーラ</p>
  <div class="abs footer-info">
    <p>大阪府緑ヶ丘市桜町1-3-4</p>
    <p class="tel">☎ 000-555-0142</p>
    <p style="margin-top:10px">営業時間</p>
    <p>【月～金】9:00～19:00（カット最終受付 18:00）</p>
    <p>【土・祝】9:00～18:00（カット最終受付 17:00）</p>
  </div>
  <a class="abs app-btn">VORA公式アプリ</a>
  <span class="abs sns" style="left:790px"></span>
  <span class="abs sns" style="left:836px"></span>
  <p class="abs sitemap-label">サイトマップ</p>
  <ul class="abs sitemap" style="left:160px">
    <li>TOP</li><li>当サロンについて</li><li>初めての方へ</li><li>頭皮・髪質改善へのこだわり</li><li>髪質のお悩み</li><li>カラーダメージのお悩み</li>
  </ul>
  <ul class="abs sitemap" style="left:500px">
    <li>頭皮のお悩み</li><li>お悩みビフォー・アフター</li><li>VORA公式アプリ</li><li>Q&amp;A</li><li>MENU・COUPON</li><li>PRODUCT</li>
  </ul>
  <ul class="abs sitemap" style="left:840px">
    <li>STAFF</li><li>VOICE</li><li>NEWS・BLOG</li><li>RECRUIT</li><li>CONTACT</li>
  </ul>
  <p class="abs copyright">© 2021 緑ヶ丘市の美容室ヴォーラ All Rights Reserved.</p>
</footer>

</body>
</html>
```